Can Design for Fun, Growing Health Food Brand

We are launching a brand new product, electrolyte seltzer drinks. We want the design to be clean/simple and slightly modern while staying true to our brand identity. Must say "Mineral Hydration" as the product descriptor, sub headline is "Carbonated electrolyte beverage with sea moss and real fruit juice". First flavors will be Watermelon Mint and Mango.

Target Market(s)

Women ages 30-50 who are interested in health wellness/trends

Industry/Entity Type

Health & Wellness

Font styles to use
Sans Serif

Requirements
Must have
• Tall, skinny can, current Bright Kelp Co Logo, use aluminum on can as element in design.
Nice to have
• Be fun, clean and modern. Would like to see the label less busy than our gels.
Should not have
• Avoid putting flavor on bottom 1/5 of can. No gradient color changes. Do not want really detailed or realistic fruit image, prefer drawings or similar.

```html
<!DOCTYPE html>
<html lang="en">
<head>
<meta charset="utf-8">
<title>Bright Kelp Co — Mineral Hydration Cans</title>
<link rel="stylesheet" href="https://fonts.googleapis.com/css2?family=Outfit:wght@300;400;500&family=Mrs+Saint+Delafield&display=swap">
<style>
  :root {
    --backdrop: #efefef;
    --alu-light: #f7f7f7;
    --alu-mid: #e4e5e5;
    --alu-edge: #cfd0d0;
    --kelp-green: #2e6b5c;
    --melon-pink: #d4838f;
    --melon-pink-deep: #b8606f;
    --mango-gold: #d8ab3c;
    --mango-gold-deep: #b48a22;
    --band-text: rgba(255,255,255,0.92);
  }
  * { margin: 0; padding: 0; box-sizing: border-box; }
  html, body { width: 1200px; height: 1039px; overflow: hidden; }
  body {
    background: var(--backdrop);
    font-family: "Outfit", sans-serif;
    position: relative;
  }
  .can {
    position: absolute;
    top: 209px;
    width: 273px;
    height: 666px;
    border-radius: 10px;
    overflow: hidden;
    background: linear-gradient(90deg, var(--alu-edge) 0%, var(--alu-light) 22%, var(--alu-mid) 55%, var(--alu-light) 78%, var(--alu-edge) 100%);
  }
  .can--watermelon { left: 255px; --flavor: var(--melon-pink); --flavor-deep: var(--melon-pink-deep); }
  .can--mango { left: 677px; --flavor: var(--mango-gold); --flavor-deep: var(--mango-gold-deep); }

  .claims {
    position: absolute;
    top: 26px;
    left: -40px;
    white-space: nowrap;
    font-size: 7.5px;
    font-weight: 500;
    letter-spacing: 1.6px;
    color: var(--kelp-green);
  }
  .claims .dot { margin: 0 10px; }

  .brand {
    position: absolute;
    top: 92px;
    left: 0; right: 0;
    display: flex;
    flex-direction: column;
    align-items: center;
    gap: 6px;
  }
  .brand-mark {
    width: 24px; height: 24px;
    border-radius: 50%;
    background: var(--kelp-green);
  }
  .brand-name {
    font-size: 12px;
    font-weight: 500;
    letter-spacing: 0.3px;
    color: var(--kelp-green);
  }

  .descriptor {
    position: absolute;
    top: 148px;
    left: 0; right: 0;
    transform: rotate(-8deg);
    font-family: "Mrs Saint Delafield", cursive;
    color: var(--kelp-green);
    line-height: 0.78;
    font-weight: 400;
  }
  .descriptor span { display: block; font-size: 76px; }
  .descriptor .line-one { padding-left: 14px; }
  .descriptor .line-two { padding-left: 36px; }

  .flavor {
    position: absolute;
    top: 274px;
    left: 0; right: 0;
    text-align: center;
    transform: rotate(-6deg);
    font-size: 8.5px;
    letter-spacing: 1.6px;
    color: var(--flavor);
  }
  .flavor::before, .flavor::after { content: "—"; margin: 0 5px; }

  .fruit-art {
    position: absolute;
    top: 322px;
    left: 56px;
    width: 162px;
    height: 130px;
    border-radius: 40% 50% 45% 55%;
    background: radial-gradient(circle at 40% 50%, var(--flavor) 0%, var(--flavor) 45%, rgba(46,107,92,0.35) 100%);
    opacity: 0.85;
  }

  .flavor-band {
    position: absolute;
    left: 0; right: 0; bottom: 0;
    height: 180px;
    background: linear-gradient(90deg, var(--flavor-deep) 0%, var(--flavor) 40%, var(--flavor-deep) 70%, var(--flavor) 100%);
  }
  .flavor-band svg { position: absolute; top: -14px; left: 0; width: 100%; height: 16px; }
  .tagline {
    position: absolute;
    top: 42px;
    left: 0; right: 0;
    text-align: center;
    font-size: 10.5px;
    font-weight: 300;
    line-height: 1.2;
    color: var(--band-text);
  }
  .volume {
    position: absolute;
    top: 116px;
    left: 0; right: 0;
    text-align: center;
    font-size: 10px;
    font-weight: 400;
    color: var(--band-text);
  }
</style>
</head>
<body>

  <article class="can can--watermelon">
    <p class="claims">NO ADDED SUGAR<span class="dot">·</span>NATURAL SEA MOSS<span class="dot">·</span>PLANT BASED</p>
    <header class="brand">
      <span class="brand-mark"></span>
      <span class="brand-name">BRIGHT KELP CO</span>
    </header>
    <h1 class="descriptor"><span class="line-one">Mineral</span><span class="line-two">Hydration</span></h1>
    <p class="flavor">WATERMELON MINT</p>
    <div class="fruit-art" role="img" aria-label="Line drawing of a watermelon slice with mint leaves and bubbles"></div>
    <section class="flavor-band">
      <svg viewBox="0 0 273 16" preserveAspectRatio="none" aria-hidden="true"><path d="M0 16 L0 8 L20 5 L40 9 L62 3 L90 8 L120 2 L150 7 L180 4 L210 9 L240 2 L273 6 L273 16 Z" fill="var(--flavor)"/></svg>
      <p class="tagline">Carbonated electrolyte<br>beverage with sea moss<br>and real fruit juice</p>
      <p class="volume">335 ml</p>
    </section>
  </article>

  <article class="can can--mango">
    <p class="claims">NO ADDED SUGAR<span class="dot">·</span>NATURAL SEA MOSS<span class="dot">·</span>PLANT BASED</p>
    <header class="brand">
      <span class="brand-mark"></span>
      <span class="brand-name">BRIGHT KELP CO</span>
    </header>
    <h1 class="descriptor"><span class="line-one">Mineral</span><span class="line-two">Hydration</span></h1>
    <p class="flavor">MANGO</p>
    <div class="fruit-art" role="img" aria-label="Line drawing of a mango with leaves and bubbles"></div>
    <section class="flavor-band">
      <svg viewBox="0 0 273 16" preserveAspectRatio="none" aria-hidden="true"><path d="M0 16 L0 8 L20 5 L40 9 L62 3 L90 8 L120 2 L150 7 L180 4 L210 9 L240 2 L273 6 L273 16 Z" fill="var(--flavor)"/></svg>
      <p class="tagline">Carbonated electrolyte<br>beverage with sea moss<br>and real fruit juice</p>
      <p class="volume">335 ml</p>
    </section>
  </article>

</body>
</html>
```